Cedar Ridge Planting Works and Sun-Sprout Megamart

The billboard will be on highway frontage and located directly next to my business building the marketing is for. The marketing on the billboard will be more directed towards the sun-sprouts megamart service being provided. And since the sign is on the businesses property it will need to say, "Exit Right Now" along with an arrow pointing to the right when facing the sign.

```html
<!DOCTYPE html>
<html lang="en">
<head>
<meta charset="utf-8">
<title>Cedar Ridge Planting Works – Sun-Sprouts Megamart Billboard</title>
<link rel="stylesheet" href="https://fonts.googleapis.com/css2?family=Montserrat:wght@700;800&family=Source+Sans+3:wght@700&display=swap">
<style>
  :root{
    --page:#929292;
    --board:#1b1b1d;
    --gold:#f2c53d;
    --white:#ffffff;
    --leaf:#7ab63f;
    --orange:#f0861e;
    --ink:#111111;
  }
  *{margin:0;padding:0;box-sizing:border-box}
  html,body{width:960px;height:1200px;overflow:hidden;background:var(--page)}
  .billboard{
    position:absolute;left:30px;top:468px;width:900px;height:263px;
    background:var(--board);overflow:hidden;
    font-family:"Montserrat",Arial,sans-serif;
  }
  .photo-strip{
    position:absolute;left:188px;top:0;width:340px;height:122px;
    background:
      radial-gradient(ellipse 38px 34px at 38% 60%, rgba(98,168,58,.95), rgba(98,168,58,0) 100%),
      radial-gradient(ellipse 70px 46px at 78% 40%, rgba(176,58,110,.9), rgba(96,140,52,.7) 55%, rgba(96,140,52,0) 100%),
      radial-gradient(ellipse 90px 60px at 40% 72%, rgba(122,86,52,.9), rgba(122,86,52,0) 100%),
      linear-gradient(90deg,#1b1b1d 0%,#2e2a22 18%,#3e3224 45%,#2a2824 75%,#1b1b1d 100%);
  }
  .brand{
    position:absolute;left:20px;top:30px;display:flex;align-items:center;gap:10px;
  }
  .brand-dot{width:22px;height:22px;border-radius:50%;background:var(--leaf);flex:none}
  .brand-name{
    color:var(--leaf);font-weight:800;font-size:21px;line-height:1.15;width:160px;
  }
  .headline{color:var(--white);font-weight:800;line-height:1}
  .headline .line-one{position:absolute;left:34px;top:127px;font-size:20px;white-space:nowrap}
  .headline .accent{color:var(--gold)}
  .headline .line-two{position:absolute;left:33px;top:153px;font-size:37px;letter-spacing:.3px}
  .tagline{
    position:absolute;left:32px;top:197px;color:var(--leaf);
    font-weight:700;font-size:13.4px;letter-spacing:.1px;white-space:nowrap;
  }
  .contact-band{
    position:absolute;left:0;top:224px;width:600px;height:39px;
    background:linear-gradient(90deg,var(--orange) 0%,var(--orange) 82%,rgba(240,134,30,0) 100%);
  }
  .contact{
    position:absolute;left:30px;top:224px;height:39px;display:flex;align-items:center;
    color:var(--ink);font-weight:800;z-index:2;white-space:nowrap;
  }
  .contact svg{flex:none}
  .phone{font-size:23px;margin-left:10px}
  .sep{width:2px;height:24px;background:var(--ink);margin:0 17px}
  .address{font-size:18px;margin-left:7px;letter-spacing:-.4px}
  .visuals{position:absolute;left:0;top:0;width:900px;height:263px}
  .exit{
    position:absolute;left:698px;top:222px;height:24px;display:flex;align-items:center;gap:9px;
    color:var(--white);font-family:"Source Sans 3",Arial,sans-serif;font-weight:700;font-size:19px;
    z-index:3;
  }
</style>
</head>
<body>
  <section class="billboard" aria-label="Sun-Sprouts Megamart highway billboard">
    <div class="photo-strip" role="img" aria-label="Photo of a green juice glass on a wooden board next to a bowl of fresh microgreens"></div>

    <div class="brand">
      <span class="brand-dot"></span>
      <span class="brand-name">Cedar Ridge Planting Works</span>
    </div>

    <h1 class="headline">
      <span class="line-one"><span class="accent">BROOKVALE'S ORGANIC</span> SUN-SPROUTS</span>
      <span class="line-two">MEGAMART</span>
    </h1>
    <p class="tagline">GET YOUR HEALTH FIX MIX OF MICRO-GREENS HERE</p>

    <div class="contact-band"></div>

    <svg class="visuals" viewBox="0 0 900 263">
      <defs>
        <radialGradient id="greens-top" cx=".45" cy=".45" r=".75">
          <stop offset="0" stop-color="#8cc63f"/>
          <stop offset=".45" stop-color="#5f9b2e"/>
          <stop offset=".75" stop-color="#8a6a44"/>
          <stop offset="1" stop-color="#4a7a22"/>
        </radialGradient>
        <radialGradient id="salad" cx=".55" cy=".5" r=".7">
          <stop offset="0" stop-color="#f0a23a"/>
          <stop offset=".35" stop-color="#b9742e"/>
          <stop offset=".6" stop-color="#4f6a2c"/>
          <stop offset="1" stop-color="#1e1e1e"/>
        </radialGradient>
        <linearGradient id="farm" x1="0" y1="0" x2="0" y2="1">
          <stop offset="0" stop-color="#f6f3fb"/>
          <stop offset=".42" stop-color="#e2dcef"/>
          <stop offset=".58" stop-color="#b9a7b4"/>
          <stop offset=".72" stop-color="#a88a86"/>
          <stop offset=".86" stop-color="#9cc45e"/>
          <stop offset="1" stop-color="#b6de7c"/>
        </linearGradient>
      </defs>
      <g role="img" aria-label="Photo of microgreen trays beside a letter board reading microgreens growing">
        <path d="M555,0 L681,0 C655,35 640,80 640,125 L511,125 C511,75 528,30 555,0 Z" fill="url(#greens-top)"/>
      </g>
      <g role="img" aria-label="Photo of a salad with roasted squash, mozzarella and microgreens on a dark plate">
        <path d="M511,129 L640,129 C642,180 672,228 720,263 L582,263 C540,232 513,185 511,129 Z" fill="url(#salad)"/>
      </g>
      <g role="img" aria-label="Photo of two workers checking crops in an indoor vertical farm under bright grow lights">
        <path d="M681,0 L900,0 L900,263 L720,263 C672,228 640,180 640,125 C640,80 655,35 681,0 Z" fill="url(#farm)"/>
      </g>
      <g fill="none" stroke="#fff" stroke-width="2.5">
        <path d="M555,0 C528,30 511,75 511,127 C511,185 540,235 582,263"/>
        <path d="M681,0 C655,35 640,80 640,125 C640,180 672,228 720,263"/>
        <line x1="511" y1="127" x2="640" y2="127" stroke-width="4"/>
      </g>
      <polygon points="676,222 862,222 862,206 899,234 862,262 862,246 692,246" fill="#000"/>
    </svg>

    <div class="contact">
      <svg width="18" height="18" viewBox="0 0 24 24" aria-hidden="true"><path d="M6.6 10.8a15.1 15.1 0 0 0 6.6 6.6l2.2-2.2a1 1 0 0 1 1-.25 11.4 11.4 0 0 0 3.6.57 1 1 0 0 1 1 1V20a1 1 0 0 1-1 1A17 17 0 0 1 3 4a1 1 0 0 1 1-1h3.5a1 1 0 0 1 1 1c0 1.25.2 2.45.57 3.57a1 1 0 0 1-.25 1z" fill="#111"/></svg>
      <span class="phone">(555)214-7730</span>
      <span class="sep"></span>
      <svg width="14" height="18" viewBox="0 0 14 20" aria-hidden="true"><path d="M7 0a7 7 0 0 0-7 7c0 5 7 13 7 13s7-8 7-13a7 7 0 0 0-7-7zm0 9.8A2.8 2.8 0 1 1 7 4.2a2.8 2.8 0 0 1 0 5.6z" fill="#111"/></svg>
      <span class="address">2460 OLD MILL ROUTE 12</span>
    </div>

    <div class="exit">
      <svg width="20" height="18" viewBox="0 0 20 18" aria-hidden="true"><path d="M1 9h16M10 2l7 7-7 7" fill="none" stroke="#fff" stroke-width="2.6" stroke-linecap="round" stroke-linejoin="round"/></svg>
      <span>Exit Right Now</span>
    </div>
  </section>
</body>
</html>
```